Dorsey K. Wendell Business Card

We need a business card for our company Dorsey K. Wendell Heating & Plumbing to be distributed to potential customers. It should follow the color scheme of our logo and have a modern upscale and masculine look.

The logo is attached and the info below should also be included:

5187 W. Cedar Brook Rd.
Linford, PA 17603

Russell T. Wendell
(717) 592-0817
russelltwendell@fernmail.net
dorseykwendell.net
PA #093148

Industry/Entity Type

Business

Contact Information for Business Card

5187 W. Cedar Brook Rd.
Linford, PA 17603

Russell T. Wendell
(717) 592-0817
russelltwendell@fernmail.net
dorseykwendell.net
PA #093148

Colors

Designer to choose colors to be used in the design.

Requirements
Must have
• Information above included

```html
<!DOCTYPE html>
<html lang="en">
<head>
<meta charset="utf-8">
<title>Dorsey K. Wendell Business Card</title>
<link rel="stylesheet" href="https://fonts.googleapis.com/css2?family=Open+Sans:wght@400;600;700&display=swap">
<style>
  :root {
    --stage: #2b2c2e;
    --navy: #1b2533;
    --navy-deep: #151d29;
    --blue: #1f5fae;
    --blue-light: #2a6cb8;
    --blue-dark: #0d4b98;
    --lime: #b6d334;
    --paper: #f1f1f1;
    --ink: #1c1c1c;
    --muted: #d9dde3;
  }
  * { box-sizing: border-box; margin: 0; padding: 0; }
  html, body { width: 1200px; height: 900px; overflow: hidden; }
  body {
    background: var(--stage);
    font-family: "Open Sans", sans-serif;
    position: relative;
  }
  .card {
    position: absolute;
    left: 320px;
    width: 560px;
    height: 320px;
    border-radius: 18px;
    overflow: hidden;
    box-shadow: 0 10px 30px rgba(0,0,0,.45);
  }
  .card-front {
    top: 100px;
    background: linear-gradient(135deg, var(--navy) 0%, #212c3b 60%, var(--navy-deep) 100%);
  }
  .card-back { top: 480px; background: var(--paper); }

  .brand {
    display: flex;
    align-items: center;
    gap: 10px;
  }
  .brand-mark {
    width: 22px; height: 22px;
    background: var(--blue);
    flex: none;
  }
  .brand-name {
    color: var(--lime);
    font-weight: 700;
    text-transform: uppercase;
    line-height: 1.2;
    letter-spacing: .5px;
  }
  .card-front .brand {
    position: absolute;
    left: 0; right: 0; top: 112px;
    justify-content: center;
  }
  .card-front .brand-name { font-size: 22px; }
  .front-web {
    position: absolute;
    left: 0; right: 0; top: 210px;
    text-align: center;
    color: var(--muted);
    font-size: 15px;
    letter-spacing: .3px;
  }

  .back-art { position: absolute; inset: 0; width: 560px; height: 320px; }
  .card-back .brand {
    position: absolute;
    left: 26px; top: 232px;
  }
  .card-back .brand-mark { width: 16px; height: 16px; }
  .card-back .brand-name { font-size: 13px; }

  .holder {
    position: absolute;
    right: 30px; top: 28px;
    text-align: right;
  }
  .holder-name { font-size: 27px; color: var(--ink); font-weight: 400; letter-spacing: -.3px; }
  .holder-role { font-size: 14px; color: var(--blue); margin-top: 2px; }
  .holder-role .sep { margin: 0 8px; }

  .contact {
    position: absolute;
    right: 30px; top: 150px;
    list-style: none;
    text-align: right;
    font-size: 13.5px;
    color: var(--ink);
    line-height: 1.45;
  }
  .contact li { display: flex; justify-content: flex-end; align-items: center; gap: 10px; }
  .contact li + li { margin-top: 4px; }
  .contact svg { width: 16px; height: 16px; flex: none; fill: var(--blue); }
</style>
</head>
<body>

<section class="card card-front" aria-label="Card front">
  <div class="brand">
    <span class="brand-mark"></span>
    <span class="brand-name">Dorsey K. Wendell<br>Heating &amp; Plumbing</span>
  </div>
  <p class="front-web">dorseykwendell.net</p>
</section>

<section class="card card-back" aria-label="Card back">
  <svg class="back-art" viewBox="0 0 560 320" aria-hidden="true">
    <defs>
      <linearGradient id="blueBand" x1="0" y1="0" x2="1" y2="0">
        <stop offset="0" stop-color="#2a6cb8"/>
        <stop offset="1" stop-color="#0d4b98"/>
      </linearGradient>
      <linearGradient id="navyBand" x1="0" y1="0" x2="1" y2="1">
        <stop offset="0" stop-color="#1b2533"/>
        <stop offset="1" stop-color="#151d29"/>
      </linearGradient>
    </defs>
    <polygon points="0,0 232,0 275,140 0,146" fill="url(#blueBand)"/>
    <polygon points="0,146 275,140 290,150 0,156" fill="#ffffff"/>
    <polygon points="0,156 290,150 340,320 0,320" fill="url(#navyBand)"/>
  </svg>

  <div class="brand">
    <span class="brand-mark"></span>
    <span class="brand-name">Dorsey K. Wendell<br>Heating &amp; Plumbing</span>
  </div>

  <div class="holder">
    <h1 class="holder-name">Russell T. Wendell</h1>
    <p class="holder-role">Job Title<span class="sep">|</span>PA #093148</p>
  </div>

  <ul class="contact">
    <li><span>5187 W. Cedar Brook Rd.<br>Linford, PA 17603</span>
      <svg viewBox="0 0 16 16"><path d="M8 0a5.5 5.5 0 0 0-5.5 5.5C2.5 10 8 16 8 16s5.5-6 5.5-10.5A5.5 5.5 0 0 0 8 0zm0 8a2.5 2.5 0 1 1 0-5 2.5 2.5 0 0 1 0 5z"/></svg></li>
    <li><span>(717) 592-0817</span>
      <svg viewBox="0 0 16 16"><path d="M1 6c0-2 3-3.5 7-3.5S15 4 15 6v1h-3.5V5.5h-7V7H1zM3.5 8h9l1.5 6H2z"/></svg></li>
    <li><span>russelltwendell@fernmail.net</span>
      <svg viewBox="0 0 16 16"><path d="M0 3h16v1.2L8 9 0 4.2z"/><path d="M0 5.6l8 4.8 8-4.8V13H0z"/></svg></li>
    <li><span>dorseykwendell.net</span>
      <svg viewBox="0 0 16 16" fill="none" stroke="#1f5fae" stroke-width="1.2"><circle cx="8" cy="8" r="7" fill="none"/><ellipse cx="8" cy="8" rx="3" ry="7" fill="none"/><path d="M1 8h14M2.2 4.5h11.6M2.2 11.5h11.6" fill="none"/></svg></li>
  </ul>
</section>

</body>
</html>
```